Web Design for Harbor Link Guild

We need a web design for Harbor Link Guild. You can see more details about the kind of business that it deals with in this link: http://harborlinkguild.ae/. The concept of the site is similar to http://www.travimo.com/ and we are looking for a homepage design also similar to it.
The top navigation should have:
1) directory
2) articles
3) deals
4) forums
5) log in/register page.
It should also have a video, a slider, map & text as well as a call to action to a "why register page".
As part of the footer it should include:
1) about HLG
2) contact HGL
3) terms & conditions
4) privacy
The color palette for the site will be the UAE flag colors which are red, green, white and black.
Updates
Project Deadline Extended
Reason: We need more designs and options.
Keep sending in more creative designs. thanks.
Industry/Entity Type
Business
Look and feel
Each slider illustrates characteristics of the customer's brand and the style your logo design should communicate.

```html
<!DOCTYPE html>
<html lang="en">
<head>
<meta charset="utf-8">
<title>Harbor Link Guild — Home</title>
<link href="https://fonts.googleapis.com/css2?family=PT+Sans:ital,wght@0,400;0,700;1,400&family=PT+Sans+Narrow:wght@400;700&display=swap" rel="stylesheet">
<style>
:root{
  --green:#05a35a;
  --green-dark:#078a4b;
  --red:#b4222a;
  --red-dark:#9c1b22;
  --ink:#333;
  --muted:#555;
  --night:#2a2a2a;
  --night-2:#3a3a3a;
  --nav-active:#5b5c60;
  --white:#fff;
}
*{box-sizing:border-box;margin:0;padding:0}
html,body{width:1200px;height:1140px;overflow:hidden;background:var(--white);font-family:"PT Sans",sans-serif;color:var(--ink)}
.page{position:relative;width:1200px;height:1140px}
.wrap{position:absolute;left:180px;width:840px}

/* header */
.site-header{position:absolute;top:0;left:0;width:1200px;height:86px}
.brand{position:absolute;left:180px;top:26px;display:flex;align-items:center;gap:10px}
.brand-mark{width:30px;height:30px;background:var(--green)}
.brand-name{font-size:24px;font-weight:700;color:var(--red);letter-spacing:.5px}
.contact{position:absolute;right:183px;top:32px;font-size:10px;color:#666;line-height:20px}
.contact-row{display:flex;align-items:center;gap:6px}
.contact svg{width:11px;height:11px;fill:#999}
.contact .gap{width:10px}

/* nav */
.main-nav{position:absolute;top:86px;left:0;width:1200px;height:38px;background:var(--green)}
.main-nav ul{list-style:none;position:absolute;left:180px;top:0;height:38px;width:840px}
.main-nav li{position:absolute;top:0;height:38px;line-height:38px;font-size:11px;font-weight:700;color:var(--white);text-align:center}
.main-nav li.active{background:var(--nav-active)}

/* hero */
.hero{top:139px;height:330px;background:linear-gradient(100deg,#ede6dc 0%,#e0d6c8 40%,#a9a39c 62%,#6e6a66 78%,#c9c4bf 100%)}
.hero-title{position:absolute;left:28px;top:118px;font-family:"PT Sans Narrow",sans-serif;font-weight:700;font-size:40px;color:var(--red);letter-spacing:-.5px}
.hero-sub{position:absolute;left:29px;top:174px;font-size:18px;line-height:25px;color:#3a3a3a}
.hero-arrows{position:absolute;right:14px;bottom:8px;display:flex;gap:12px}
.hero-arrows svg{width:8px;height:10px;stroke:#fff;fill:none;stroke-width:1.2}

/* cta band */
.cta-band{top:470px;height:86px;display:flex}
.cta{display:flex;flex:1}
.cta-body{flex:1;padding:17px 0 0 23px;color:var(--white)}
.cta-body h3{font-size:16px;font-weight:400;letter-spacing:.3px;margin-bottom:5px}
.cta-body p{font-size:7.6px;line-height:15px;text-transform:uppercase}
.cta-btn{width:103px;display:flex;align-items:center;justify-content:center;color:var(--white);font-family:"PT Sans Narrow",sans-serif;font-size:12px;font-weight:700}
.cta.deals{background:var(--green)}
.cta.deals .cta-btn{background:var(--green-dark)}
.cta.register{background:var(--red)}
.cta.register .cta-btn{background:var(--red-dark)}

/* content */
.section-title{position:absolute;font-size:16px;font-weight:700;color:var(--green);top:576px}
.how{left:180px}
.about-title{left:559px}
.video{position:absolute;left:180px;top:611px;width:343px;height:205px;border:1px solid #ccc}
.video-frame{position:absolute;inset:0 0 20px 0;background:linear-gradient(120deg,#d9dcdf,#b8b4b0 45%,#e6e6e6)}
.video-controls{position:absolute;left:0;right:0;bottom:0;height:20px;background:#f1f1f1;border-top:1px solid #ccc;display:flex;align-items:center;font-size:9px;font-weight:700;color:#222}
.video-controls .play{width:20px;display:flex;justify-content:center;border-right:1px solid #ccc;height:100%;align-items:center}
.video-controls .time{padding:0 7px}
.video-controls .track{flex:1;height:4px;background:#c9c9c9}
.video-controls .icon{width:30px;height:100%;border-left:1px solid #ccc;display:flex;align-items:center;justify-content:center}
.about{position:absolute;left:559px;top:610px;width:461px;font-size:8.6px;line-height:15.5px;color:var(--muted)}
.about p+p{margin-top:15px}
.more-btn{position:absolute;left:559px;top:767px;width:180px;height:33px;background:var(--red);color:var(--white);font-size:10.5px;display:flex;align-items:center;justify-content:center;border-radius:2px}

/* recent deals */
.recent{position:absolute;top:843px;left:0;width:1200px;height:223px;background:var(--night)}
.recent h2{position:absolute;left:180px;top:18px;font-size:16px;font-weight:700;color:var(--white)}
.recent-arrows{position:absolute;left:979px;top:18px;display:flex;gap:2px}
.recent-arrows span{width:20px;height:20px;background:var(--night-2);display:flex;align-items:center;justify-content:center}
.recent-arrows svg{width:6px;height:8px;stroke:#ccc;fill:none;stroke-width:1.2}
.deal{position:absolute;top:54px;width:199px}
.deal-photo{height:106px}
.deal p{margin-top:10px;padding-left:3px;font-size:8.6px;font-style:italic;line-height:15px;color:#bdbdbd}

/* footer */
.site-footer{position:absolute;top:1066px;left:0;width:1200px;height:74px;background:var(--green);color:var(--white)}
.footer-links{position:absolute;left:182px;top:22px;display:flex;font-size:7.6px;text-transform:uppercase}
.footer-links span{padding:0 18px}
.footer-links span:first-child{padding-left:0}
.footer-links .sep{padding:0}
.copyright{position:absolute;left:182px;top:44px;font-size:7.4px;text-transform:uppercase}
.social{position:absolute;right:182px;top:22px;display:flex;align-items:center;gap:5px}
.social-label{font-size:7.4px;text-align:right;line-height:15px;margin-right:7px;text-transform:uppercase}
.social i{width:25px;height:25px;border-radius:50%;display:block}
</style>
</head>
<body>
<div class="page">

  <header class="site-header">
    <div class="brand"><span class="brand-mark"></span><span class="brand-name">HARBOR LINK GUILD</span></div>
    <div class="contact">
      <div class="contact-row">
        <svg viewBox="0 0 12 12"><path d="M2 1h3l1 3-1.5 1a6 6 0 0 0 2.5 2.5L8 6l3 1v3a1 1 0 0 1-1 1A9 9 0 0 1 1 2a1 1 0 0 1 1-1z"/></svg>
        <span>+971 (4) 300 1840,</span><span class="gap"></span>
        <svg viewBox="0 0 12 12"><rect x="3" y="1" width="6" height="3"/><rect x="1" y="4" width="10" height="5"/><rect x="3" y="8" width="6" height="3"/></svg>
        <span>+971 (4) 300 1841</span>
      </div>
      <div class="contact-row">
        <svg viewBox="0 0 12 12"><rect x="1" y="2" width="10" height="8" fill="none" stroke="#999"/><path d="M1 2l5 4 5-4" fill="none" stroke="#999"/></svg>
        <span>nadia@harborlinkguild.ae</span>
      </div>
    </div>
  </header>

  <nav class="main-nav">
    <ul>
      <li class="active" style="left:0;width:130px">HOME</li>
      <li style="left:148px;width:120px">DIRECTORY</li>
      <li style="left:300px;width:80px">ARTICLES</li>
      <li style="left:420px;width:80px">DEALS</li>
      <li style="left:540px;width:90px">FORUMS</li>
      <li style="left:680px;width:120px">LOG IN/REGISTER</li>
    </ul>
  </nav>

  <section class="wrap hero" role="img" aria-label="Photo of two businessmen reviewing work at an office desk">
    <h1 class="hero-title">HARBOR LINK GUILD</h1>
    <p class="hero-sub">PROVIDE A SUPPORTIVE INFRASTRUCTURE<br>TO ENABLE COMPANIES</p>
    <div class="hero-arrows">
      <svg viewBox="0 0 8 10"><path d="M6 1L2 5l4 4"/></svg>
      <svg viewBox="0 0 8 10"><path d="M2 1l4 4-4 4"/></svg>
    </div>
  </section>

  <section class="wrap cta-band">
    <div class="cta deals">
      <div class="cta-body"><h3>DEALS</h3><p>Provide a supportive infrastructure to enable companies to access<br>and engage in unlimited networking opportunities.</p></div>
      <div class="cta-btn">CLICK HERE</div>
    </div>
    <div class="cta register">
      <div class="cta-body"><h3>WHY REGISTER ?</h3><p>Provide a supportive infrastructure to enable companies to access<br>and engage in unlimited networking opportunities.</p></div>
      <div class="cta-btn">CLICK HERE</div>
    </div>
  </section>

  <h2 class="section-title how">HOW IT WORKS</h2>
  <h2 class="section-title about-title">ABOUT HARBOR LINK GUILD</h2>

  <div class="video">
    <div class="video-frame" role="img" aria-label="Video still of a smiling group of business colleagues"></div>
    <div class="video-controls">
      <span class="play"><svg width="7" height="8" viewBox="0 0 7 8"><path d="M0 0l7 4-7 4z" fill="#111"/></svg></span>
      <span class="time">00:00</span>
      <span class="track"></span>
      <span class="time">00:00</span>
      <span class="icon"><svg width="22" height="8" viewBox="0 0 22 8"><path d="M0 3h2l2-2v6L2 5H0z" fill="#111"/><path d="M7 6v1M9 5v2M11 4v3M13 3v4M15 2v5M17 1v6M19 0v7" stroke="#111"/></svg></span>
      <span class="icon"><svg width="9" height="9" viewBox="0 0 9 9" fill="none" stroke="#111"><path d="M1 3V1h2M6 1h2v2M8 6v2H6M3 8H1V6"/></svg></span>
    </div>
  </div>

  <div class="about">
    <p>It is a long established fact that a reader will be distracted by the readable content of a page when looking at its layout. The point of using Lorem Ipsum is that it has a more-or-less normal distribution of letters, as opposed to using 'Content here, content here', making it look like readable English. Many desktop publishing packages and web page editors now use Lorem Ipsum as their default model text, and a search for 'lorem ipsum' will uncover many web sites still in their infancy. Various versions have evolved over the years, sometimes by accident, sometimes on purpose.</p>
    <p>Many desktop publishing packages and web page editors now use Lorem Ipsum as their default model text, and a search for 'lorem ipsum' will uncover many web sites still in their infancy. Various versions have evolved over the years, sometimes by accident, sometimes on purpose.</p>
  </div>
  <div class="more-btn">CLICK HERE FOR MORE INFO</div>

  <section class="recent">
    <h2>RECENT DEALS</h2>
    <div class="recent-arrows">
      <span><svg viewBox="0 0 6 8"><path d="M5 0L1 4l4 4"/></svg></span>
      <span><svg viewBox="0 0 6 8"><path d="M1 0l4 4-4 4"/></svg></span>
    </div>
    <div class="deal" style="left:180px">
      <div class="deal-photo" role="img" aria-label="Photo of colleagues gathered around a phone" style="background:linear-gradient(120deg,#cfc9c2,#8f8a86 50%,#e3e0dc)"></div>
      <p>A business Networking Platform helping Harbor Link Guild members' source new customers.</p>
    </div>
    <div class="deal" style="left:394px">
      <div class="deal-photo" role="img" aria-label="Photo of a senior businessman in an office" style="background:linear-gradient(120deg,#d7d8dc,#8e949e 55%,#c0c8d2)"></div>
      <p>A business Networking Platform helping Harbor Link Guild members' source new customers.</p>
    </div>
    <div class="deal" style="left:607px">
      <div class="deal-photo" role="img" aria-label="Photo of hands reviewing a bar chart beside a laptop" style="background:linear-gradient(120deg,#e9e4de,#f4f4f4 50%,#b9b7b5)"></div>
      <p>A business Networking Platform helping Harbor Link Guild members' source new customers.</p>
    </div>
    <div class="deal" style="left:821px">
      <div class="deal-photo" role="img" aria-label="Photo of a man working on a laptop on a sofa" style="background:linear-gradient(120deg,#f2f2f2,#c7ccd3 55%,#eeeeee)"></div>
      <p>A business Networking Platform helping Harbor Link Guild members' source new customers.</p>
    </div>
  </section>

  <footer class="site-footer">
    <div class="footer-links">
      <span>About HLG</span><span class="sep">|</span>
      <span>Contact HGL</span><span class="sep">|</span>
      <span>Terms &amp; Conditions</span><span class="sep">|</span>
      <span>Privacy</span>
    </div>
    <p class="copyright">© Copyright 2013. Harbor Link Guild. All rights reserved.</p>
    <div class="social">
      <div class="social-label">Connect to<br>our social network :</div>
      <i style="background:#2f5fa8"></i>
      <i style="background:#3aa7dd"></i>
      <i style="background:#1d74a8"></i>
      <i style="background:#e59a1c"></i>
      <i style="background:#d42a26"></i>
    </div>
  </footer>

</div>
</body>
</html>
```